Executive & Leadership Coach needs a Graphic Design

We need a graphic design for a Leadership methodology/strategy that can be linked to The Summit Compass

The Summit Compass consists of:
1. Achievements
2. Personal Brand
3. Network
4. Executive Presence

This should Graphic Design will need to be used in PowerPoint presentations, training manuals and web pages

The design should be modern and provide the feeling of strength, trust, energy & creativity

Industry/Entity Type

Graphic Design

Font styles to use
Other font styles liked:
• Calibri, Verdana

```html
<!DOCTYPE html>
<html lang="en">
<head>
<meta charset="utf-8">
<title>The Summit Compass</title>
<link rel="stylesheet" href="https://fonts.googleapis.com/css2?family=Open+Sans:wght@400;700&display=swap">
<style>
  :root {
    --page-bg: #f4f4f4;
    --ring: #ffffff;
    --blue-deep: #1a6cb8;
    --blue-light: #27ade3;
    --green-main: #8dc63f;
    --green-bright: #c9dd2a;
    --purple-deep: #662d91;
    --purple-light: #93298f;
    --pink-deep: #dc1a5a;
    --pink-bright: #e6007e;
    --hub-text: #3a3a3a;
    --label-text: #ffffff;
  }
  html, body {
    margin: 0;
    padding: 0;
    width: 1200px;
    height: 1000px;
    overflow: hidden;
    background: var(--page-bg);
  }
  .compass {
    display: block;
    width: 1200px;
    height: 1000px;
  }
  .segment-label {
    font-family: "Open Sans", "Segoe UI", sans-serif;
    font-size: 37px;
    font-weight: 400;
    fill: var(--label-text);
    letter-spacing: 0.5px;
  }
  .hub-title {
    font-family: "Open Sans", "Calibri", sans-serif;
    font-size: 34px;
    font-weight: 700;
    fill: var(--hub-text);
  }
</style>
</head>
<body>
<svg class="compass" viewBox="0 0 1200 1000" xmlns="http://www.w3.org/2000/svg" role="img" aria-label="The Summit Compass: Executive Presence, Achievements, Network, Personal Brand">
  <defs>
    <linearGradient id="grad-presence" x1="0" y1="0" x2="1" y2="1">
      <stop offset="0" stop-color="var(--blue-deep)"/>
      <stop offset="0.75" stop-color="var(--blue-light)"/>
      <stop offset="1" stop-color="var(--blue-light)"/>
    </linearGradient>
    <linearGradient id="grad-achievements" x1="0" y1="1" x2="1" y2="0">
      <stop offset="0" stop-color="var(--green-bright)"/>
      <stop offset="0.45" stop-color="var(--green-main)"/>
      <stop offset="1" stop-color="var(--green-main)"/>
    </linearGradient>
    <linearGradient id="grad-network" x1="0" y1="0" x2="1" y2="1">
      <stop offset="0" stop-color="var(--purple-light)"/>
      <stop offset="0.45" stop-color="var(--purple-deep)"/>
      <stop offset="1" stop-color="var(--purple-deep)"/>
    </linearGradient>
    <linearGradient id="grad-brand" x1="1" y1="0" x2="0" y2="1">
      <stop offset="0" stop-color="var(--pink-bright)"/>
      <stop offset="1" stop-color="var(--pink-deep)"/>
    </linearGradient>
    <radialGradient id="grad-hub" cx="0.5" cy="0.5" r="0.5">
      <stop offset="0.75" stop-color="#ffffff"/>
      <stop offset="1" stop-color="#e4e4e4"/>
    </radialGradient>
    <filter id="soft-shadow" x="-20%" y="-20%" width="140%" height="140%">
      <feDropShadow dx="8" dy="10" stdDeviation="8" flood-color="#000" flood-opacity="0.28"/>
    </filter>
    <filter id="hub-shadow" x="-30%" y="-30%" width="160%" height="160%">
      <feDropShadow dx="0" dy="0" stdDeviation="6" flood-color="#000" flood-opacity="0.3"/>
    </filter>
    <path id="arc-top" d="M 315 500 A 285 285 0 0 1 885 500"/>
    <path id="arc-bottom" d="M 300 500 A 300 300 0 0 0 900 500"/>
  </defs>

  <circle class="outer-ring" cx="600" cy="500" r="345" fill="var(--ring)" filter="url(#soft-shadow)"/>

  <g class="segments" stroke="#ffffff" stroke-width="3">
    <path class="segment segment-presence" d="M600 500 L267 500 A333 333 0 0 1 600 167 Z" fill="url(#grad-presence)"/>
    <path class="segment segment-achievements" d="M600 500 L600 167 A333 333 0 0 1 933 500 Z" fill="url(#grad-achievements)"/>
    <path class="segment segment-network" d="M600 500 L933 500 A333 333 0 0 1 600 833 Z" fill="url(#grad-network)"/>
    <path class="segment segment-brand" d="M600 500 L600 833 A333 333 0 0 1 267 500 Z" fill="url(#grad-brand)"/>
  </g>

  <g class="segment-labels">
    <text class="segment-label"><textPath href="#arc-top" startOffset="169" text-anchor="middle">Executive Presence</textPath></text>
    <text class="segment-label"><textPath href="#arc-top" startOffset="680" text-anchor="middle">Achievements</textPath></text>
    <text class="segment-label"><textPath href="#arc-bottom" startOffset="733" text-anchor="middle">Network</textPath></text>
    <text class="segment-label"><textPath href="#arc-bottom" startOffset="245" text-anchor="middle">Personal Brand</textPath></text>
  </g>

  <g class="hub">
    <circle cx="600" cy="500" r="123" fill="url(#grad-hub)" stroke="#ffffff" stroke-width="4" filter="url(#hub-shadow)"/>
    <text class="hub-title" x="600" y="490" text-anchor="middle">Summit</text>
    <text class="hub-title" x="600" y="532" text-anchor="middle">Compass</text>
  </g>
</svg>
</body>
</html>
```